Marketing Collaterals
Flyer, edm, web template, product label, brochure, vouchers
Hi Brondel,
Thanks for your new submissions. I like the look and feel of this set of collaterals. But as mentioned, no need to work on flyer and label.
And pls make the voucher generic so I can stamp the value of the voucher on it. Pls also make the voucher simpler and cleaner looking.
Thanks
HI Everyone,
Just to reiterate:
No need to work on flyer, product label, edm anymore.
Only need to work on the following in order of priority:
1) Website
2) Vouchers (1 generic version that I can rubber stamp value of voucher on it) pls take note of size - 148.5 mm x 70 mm
3) Brochure
Thanks.
Hi everyone,
I also noticed many of you used a lot of curves and wavy lines. I much prefer simple, clean cut straight lines. With a zen feel.
The closest to it now is probably #25.
The offer posters that I uploaded as well as the stock images should give you a clear idea of what I'm looking for.
Thanks again.
I also noticed that many of you used images that are not quite suitable. Either because they are too feminine, or contradicts the services we provide. Eg. our upper body massages are provided on chairs, so images of people lying on their back while receiving a massage may be misleading.
To make it easier for all, I have gone to Pixelharbor to look for suitable images. Here is the link to my lightbox http://www.pixelharbor-example.com/public_lightbox.mhtml?lightbox_id=48207615&code=3ac19b8e2d4470fa61c8e3907b15d2c4
Pls limit images to those in the light box instead.
Pls let me know if the link to the lightbox is not working.
Hi Everyone,
Hope you had a great start to the new year.
I am sorry for keeping all of you waiting. My business start up is going through some teething problems that prevented me from devoting time to work on the marketing collaterals. Thank you all for your patience and understanding.
And I thank the staff @ Plenvarta for allowing me to reopen this project.
To keep the project more focussed and simpler, I have decided to drop several of the items in the original scope of work, leaving only 3 items. Pls see below for update:
Items to work on in order of priority:
1)Website template
- I have uploaded an updated copy for the website
- Look and feel should be simple, clean and sophisticated
- Main colour will be black
- I have uploaded my business card, the label for the Dead Sea Salt packaging as well as 2 offer posters for your reference so you know what kind of look I am going for
2) Gift Vouchers
- Dimensions: 148.5 mm x 70 mm
- 4 colour x 1 colour
- back of the voucher will feature terms and conditions
- To save on print cost, I would like to have one single version of the voucher, with the flexibility to rubber stamp the value of the voucher. (pls let me know if this is not clear and I will be happy to clarify what I mean)
- Voucher value could include: $5 spa cash, $50 spa cash, 40 mins Foot Reflexology, 20 mins Upper Body Massage etc. These values will be rubber stamped prominently onto the generic voucher.
- Dimension: Open size - 210mm x 297mm
Closed size - 210mm x 99mm
- Brochure should follow the look and feel of the website
- Copy will need to be cut back quite a bit
Hope this provides clearer direction now.
Thank you and I look forward to seeing your work.
Hi to all designers who submitted your designs. I have been very bogged down by a series of unexpected issues on the business front. Hence have not devote time to work on this. Will look into this as soon as I can.
To staff of plenvarta, i understand I would normally have 7 days to decide but I need more time. I will come back as soon as I can.
Thanks to all for understanding.
Thanks to all designers who submitted your designs. Apologies for not getting back and providing feedback on your designs as I have been very busy with the opening of the shop.
Am looking through all of your work now. Will come back soon.
kindly send feedback on the above entries. thanks
Working on it :)
Dear Project Holder,
I saw your project.I am working on it.thanks.
Hi NimbusForgeArt,
Thank you for your submission.
Here are my comments:
#1 - As mentioned, the images of the ladies are not very appropriate and does not align with the offerings and image of the place we want to portray.
#2 - Same comments on the images of the ladies. Also, one side of the flyer should introduce Kelp Arbor and it's services and the other side is purely on the offers.
#3 - Many of images used are again not suitable as they are not part of our service offering and some of the fish therapy pictures feature the wrong type of fish.
Tip: Keep the creatives clean. Maybe better to have few but bigger appropriate pictures then to have many small pictures.
Hope the comments are helpful.
Thank you.
Hi Rovantoad,
I had every intention to award the job at the end. But if it makes it more secure, I have now guaranteed the job. I have also increased the prize money from $400 previously to $800 now.
Thanks for the feedback and hope to see your submission.
Hi all,
I need to add one more item:
Promotional pull up banner standee
It will feature the 2 promotional offers as stated in the flyer.
Also, pls note that for the A5 flyer, my preference is for it to be portrait rather than landscape.
Dear 7pixelcrafter and Brondel,
Thanks for your feedback. I have increased the prize money.
Hope to see your work soon.

```html
<!DOCTYPE html>
<html lang="en">
<head>
<meta charset="utf-8">
<title>Kelp Arbor Brochure</title>
<link href="https://fonts.googleapis.com/css2?family=Open+Sans:wght@400;600;700&display=swap" rel="stylesheet">
<style>
:root{
  --teal:#2aa6c4;
  --green:#8cc63f;
  --pink:#e0338a;
  --ink:#2b2b2b;
  --ink-soft:#555555;
  --black:#111111;
  --paper:#ffffff;
  --bg:#ffffff;
  --skin-a:#e9cdbd;
  --skin-b:#b98c76;
}
*{box-sizing:border-box;margin:0;padding:0}
html,body{width:1200px;height:1033px;overflow:hidden;background:var(--bg)}
body{position:relative;font-family:"Open Sans",Arial,sans-serif;color:var(--ink)}
.sheet{position:absolute;background:var(--paper);box-shadow:0 2px 8px rgba(0,0,0,.25);overflow:hidden}
.top-band{position:absolute;left:0;top:0;width:100%;height:26px;background:var(--teal);border-bottom:4px solid var(--green)}
.foot-band{position:absolute;left:0;bottom:0;width:100%;height:10px;background:var(--teal)}
.photo{position:absolute}
.photo-face{background:linear-gradient(120deg,#eef4f6 0%,var(--skin-a) 42%,#6b4a3c 78%,#2d211c 100%)}
.photo-hands{background:linear-gradient(160deg,#f3e2d7 0%,var(--skin-a) 50%,var(--skin-b) 100%)}
.photo-flowers{background:radial-gradient(circle at 35% 40%,#e86aa8 0%,#c95a9a 25%,#7b6b63 60%,#cfc7c0 100%)}
.photo-feet{background:radial-gradient(circle at 50% 50%,#f1d6c6 0%,var(--skin-a) 40%,#9b7b86 75%,#e8e2e4 100%)}
.photo-fish{background:linear-gradient(180deg,#bfe0e6 0%,#8fb8bd 50%,#d9c3b2 100%)}
.photo-round{border-radius:50%;background:radial-gradient(circle,#f0d8c8 0%,var(--skin-b) 80%)}
.panel-text{position:absolute;font-size:7px;line-height:1.6;color:var(--ink-soft)}
.panel-text p{margin-bottom:6px}
.heading{color:var(--pink);font-weight:600;line-height:1.15}
.heading small{display:block;font-weight:400;font-size:.75em;margin-top:2px}
.brand-name{position:absolute;font-weight:700;color:var(--teal);white-space:nowrap;display:flex;align-items:center;gap:.35em;line-height:1}
.brand-dot{display:inline-block;border-radius:50%;background:var(--teal)}
.address{position:absolute;font-size:6.5px;line-height:1.6;text-align:center;color:var(--ink-soft)}
.rule{position:absolute;height:1px;background:var(--black)}
</style>
</head>
<body>

<!-- Outside spread -->
<section class="sheet outside-spread" style="left:23px;top:29px;width:486px;height:480px">
  <div class="top-band"></div>
  <div class="photo photo-face" role="img" aria-label="Woman with eyes closed receiving a neck massage" style="left:162px;top:30px;width:324px;height:330px"></div>
  <div class="panel-text" style="left:12px;top:44px;width:140px">
    <div class="heading" style="font-size:13px;margin-bottom:8px">Kelp Arbor<small style="font-size:12px">A Retreat for<br>Body &amp; Soul</small></div>
    <p>Step away from the rush of the city and rest your tired feet. Our calm rooms, trained therapists and gentle rituals help you unwind, restore balance and leave feeling light again.</p>
    <p>Every visit starts with a warm welcome, a cup of herbal tea and a quiet moment to settle in before your treatment begins.</p>
    <p>Walk in any day of the week. No booking is needed for short sessions, and gift vouchers are available at the counter.</p>
  </div>
  <div class="photo photo-hands" role="img" aria-label="Hands massaging a shoulder" style="left:0;top:262px;width:200px;height:208px"></div>
  <div class="brand-name" style="left:232px;top:378px;font-size:18px"><span class="brand-dot" style="width:12px;height:12px"></span>Kelp Arbor</div>
  <div class="rule" style="left:232px;top:404px;width:120px"></div>
  <div class="address" style="left:212px;top:412px;width:160px">12 Linden Quay #01-08<br>Open daily 10am to 10pm<br>Tel: 6550 0000</div>
  <div class="foot-band"></div>
</section>

<!-- Closed brochure, front -->
<section class="sheet closed-front" style="left:557px;top:171px;width:172px;height:358px">
  <div class="top-band"></div>
  <div class="photo photo-face" role="img" aria-label="Woman receiving a shoulder massage" style="left:0;top:30px;width:172px;height:290px"></div>
  <div class="brand-name" style="left:20px;top:330px;font-size:17px"><span class="brand-dot" style="width:11px;height:11px"></span>Kelp Arbor</div>
</section>

<!-- Closed brochure, back -->
<section class="sheet closed-back" style="left:757px;top:43px;width:186px;height:343px">
  <div class="top-band"></div>
  <div class="photo photo-face" role="img" aria-label="Woman with eyes closed, relaxed" style="left:0;top:30px;width:186px;height:270px"></div>
  <div class="brand-name" style="left:26px;top:312px;font-size:18px"><span class="brand-dot" style="width:11px;height:11px"></span>Kelp Arbor</div>
</section>

<!-- Inside spread -->
<section class="sheet inside-spread" style="left:23px;top:537px;width:563px;height:477px">
  <div class="top-band"></div>

  <div class="photo photo-flowers" role="img" aria-label="Pink orchids and spa stones" style="left:0;top:30px;width:188px;height:128px"></div>
  <div class="panel-text" style="left:12px;top:170px;width:164px">
    <div class="heading" style="font-size:12px;margin-bottom:8px">Foot Reflexology<small>The Natural Way To Wellbeing</small></div>
    <p>Pressure applied to points on the feet eases tension across the whole body. Each session begins with a warm soak and ends with a calming herbal balm.</p>
    <p>Our therapists trace the map of the foot with care, easing aches from long walks, tight shoes and busy days on your feet.</p>
    <p>Many guests find they sleep more deeply, feel lighter and move with greater ease after only a few visits.</p>
    <p>Choose from 40 or 60 minute treatments, or pair a session with an upper body massage for a full reset.</p>
    <p>Regular guests may ask about our loyalty card, which rewards every tenth visit with a free session.</p>
  </div>

  <div class="photo photo-feet" role="img" aria-label="Feet resting beside orchids" style="left:196px;top:30px;width:180px;height:176px"></div>
  <div class="panel-text" style="left:202px;top:218px;width:166px">
    <div class="heading" style="font-size:12px;margin-bottom:8px">Upper Body Massage<small>Rub Those Cares Away</small></div>
    <p>Seated on our ergonomic chairs, you stay fully clothed while skilled hands work the neck, shoulders and back to release knots built up from long days at the desk.</p>
    <p>Sessions are short enough for a lunch break yet deep enough to leave you refreshed and ready for the afternoon.</p>
    <p>Ask your therapist for firm or gentle pressure, and let us know of any areas that need extra attention.</p>
    <p>Available in 10, 20 and 30 minute sessions.</p>
  </div>

  <div class="panel-text" style="left:388px;top:42px;width:164px">
    <div class="heading" style="font-size:12px;margin-bottom:8px">Fish Spa<small>The Natural Pedicure</small></div>
    <p>Dip your feet into clear, filtered pools where gentle garra rufa fish nibble away dead skin, leaving feet smooth and soft.</p>
    <p>The light tickle soon turns into a soothing, relaxing feeling that guests of all ages enjoy.</p>
  </div>
  <div class="photo photo-fish" role="img" aria-label="Feet in a fish spa pool" style="left:388px;top:150px;width:164px;height:118px"></div>
  <div class="panel-text" style="left:388px;top:278px;width:164px">
    <p>Every pool is cleaned and refreshed daily for your comfort and hygiene, and each guest rinses before entering the water.</p>
    <p>Sessions run for 15 or 30 minutes and can be added to any treatment.</p>
  </div>
  <div class="photo photo-round" role="img" aria-label="Close-up of a relaxing treatment" style="left:428px;top:360px;width:88px;height:88px"></div>

  <div class="foot-band"></div>
</section>

<!-- Brand name -->
<div class="brand-name" style="left:700px;top:800px;font-size:58px"><span class="brand-dot" style="width:40px;height:40px"></span>Kelp Arbor</div>

</body>
</html>
```